Vertical Design 11.5"x 84"

this project is going to be 12 different design panels that will go in our retail store, Talvon Guard Doors. These designs will be 11.5" x 84" and will be displayed with our doors. https://talvonguarddoors.example/
There are 12 places in our door displays to put these graphics. See our photo demonstrating where the graphics will go.
Ideas for the graphics:
1. image backgrounds can be brick, vinyl siding, split shake siding, in various colors and styles, sunny day, flowery grassy meadow, use your imagination.
2. graphics can be words and phrases like - Made In The USA, Custom Sizes,
3. Images used can be entry doors side-lites, security side-lites (see photo of door with 2 security side lites)
All these graphics are about entry doors, security doors, and patio doors.
Use vibrant colors, things that are exciting. There's 12 different panels so use your creativity to mix it up.
You can use the bee guy theme that was created in the past that would be great to add continuity to our marketing.
Target Market(s)
HOME OWNERS
Look and feel
Each slider illustrates characteristics of the customer's brand and the style your logo design should communicate.

```html
<!DOCTYPE html>
<html lang="en">
<head>
<meta charset="utf-8">
<title>Talvon Guard Doors – Display Panels 11.5 x 84</title>
<link rel="stylesheet" href="https://fonts.googleapis.com/css2?family=Orbitron:wght@600;700&family=Arimo:wght@400&display=swap">
<style>
  :root{
    --brand-yellow:#FFD400;
    --brand-yellow-light:#FFE85A;
    --brand-black:#0D0D0D;
    --brand-black-light:#3A3A3A;
    --badge-white:#FFFFFF;
    --dim-grey:#6B6B6B;
    --page:#FFFFFF;
  }
  html,body{margin:0;padding:0;overflow:hidden;}
  body{width:829px;height:1200px;background:var(--page);position:relative;}
  .gradients{position:absolute;width:0;height:0;}
  .panel{position:absolute;width:66.3px;display:block;}
  .row-top{top:100.5px;height:494.4px;}
  .row-bottom{top:639.3px;height:500.8px;}
  .col-1{left:117.5px}.col-2{left:224.1px}.col-3{left:330.7px}
  .col-4{left:437.2px}.col-5{left:543.3px}.col-6{left:649.9px}
  .fill-yellow{fill:var(--brand-yellow)}
  .fill-black{fill:var(--brand-black)}
  .panel-title{font-family:'Orbitron',sans-serif;font-weight:700;font-size:54px;}
  .badge-circle{fill:var(--badge-white);}
  .badge-name{font-family:'Orbitron',sans-serif;font-weight:700;fill:var(--brand-black);text-anchor:middle;}
  .dimension{position:absolute;font-family:'Arimo',sans-serif;font-size:11px;color:#333;}
  .dim-line{position:absolute;background:var(--dim-grey);}
</style>
</head>
<body>

<svg class="gradients" aria-hidden="true">
  <defs>
    <radialGradient id="grad-black" cx="50%" cy="50%" r="60%">
      <stop offset="0" stop-color="var(--brand-black-light)"/>
      <stop offset="1" stop-color="var(--brand-black)"/>
    </radialGradient>
    <radialGradient id="grad-yellow" cx="50%" cy="50%" r="60%">
      <stop offset="0" stop-color="var(--brand-yellow-light)"/>
      <stop offset="1" stop-color="var(--brand-yellow)"/>
    </radialGradient>
  </defs>
</svg>

<!-- dimension marks -->
<div class="dimension" style="left:139px;top:67px;">11,5</div>
<div class="dim-line" style="left:117.5px;top:82.5px;width:66.3px;height:0.7px;"></div>
<div class="dim-line" style="left:117.5px;top:73px;width:0.7px;height:17px;"></div>
<div class="dim-line" style="left:183.5px;top:73px;width:0.7px;height:17px;"></div>
<div class="dimension" style="left:76px;top:341px;">84</div>
<div class="dim-line" style="left:100.3px;top:100.5px;width:0.7px;height:494.4px;"></div>
<div class="dim-line" style="left:92px;top:100.5px;width:17px;height:0.7px;"></div>
<div class="dim-line" style="left:92px;top:594.5px;width:17px;height:0.7px;"></div>

<!-- Row 1 -->
<svg class="panel row-top col-1" viewBox="0 0 127 925" preserveAspectRatio="none">
  <rect width="127" height="925" fill="url(#grad-black)"/>
  <path class="fill-yellow" d="M0,0H127V82C90,42 40,28 0,35Z"/>
  <path class="fill-yellow" d="M0,222C25,150 70,100 127,92V110C80,116 30,165 0,240Z"/>
  <path class="fill-yellow" d="M0,770C25,805 65,832 127,838V862C80,850 40,835 0,808Z"/>
  <path class="fill-yellow" d="M0,885C50,870 95,872 127,880V925H0Z"/>
  <text class="panel-title fill-yellow" transform="translate(80,647) rotate(-90)" textLength="465" lengthAdjust="spacingAndGlyphs">CUSTOM SIZE</text>
  <circle class="badge-circle" cx="65" cy="720" r="45"/>
  <text class="badge-name" x="65" y="717" font-size="14">TALVON</text>
  <text class="badge-name" x="65" y="733" font-size="9">GUARD DOORS</text>
</svg>

<svg class="panel row-top col-2" viewBox="0 0 127 925" preserveAspectRatio="none">
  <rect width="127" height="925" fill="url(#grad-yellow)"/>
  <path class="fill-black" d="M0,0H127V60C85,62 40,45 0,35Z"/>
  <path class="fill-black" d="M0,70C40,85 90,95 127,95V145C80,150 30,120 0,105Z"/>
  <path class="fill-black" d="M0,860C50,840 100,790 127,735V840C90,860 45,870 0,880Z"/>
  <path class="fill-black" d="M0,895C45,880 95,885 127,905V925H0Z"/>
  <text class="panel-title fill-black" transform="translate(81,714) rotate(-90)" textLength="554" lengthAdjust="spacingAndGlyphs">DURABLE SAFETY</text>
  <circle class="badge-circle" cx="63" cy="780" r="45"/>
  <text class="badge-name" x="63" y="777" font-size="14">TALVON</text>
  <text class="badge-name" x="63" y="793" font-size="9">GUARD DOORS</text>
</svg>

<svg class="panel row-top col-3" viewBox="0 0 127 925" preserveAspectRatio="none">
  <rect width="127" height="925" fill="url(#grad-black)"/>
  <path class="fill-yellow" d="M0,0H127V25C80,15 35,15 0,22Z"/>
  <path class="fill-yellow" d="M0,118C40,75 80,45 127,40V58C80,65 40,90 0,120Z"/>
  <path class="fill-yellow" d="M0,808C50,795 100,815 127,848V865C90,840 40,830 0,838Z"/>
  <path class="fill-yellow" d="M0,845C45,845 95,880 127,878V925H0Z"/>
  <text class="panel-title fill-yellow" transform="translate(79,672) rotate(-90)" textLength="584" lengthAdjust="spacingAndGlyphs">SAFE PROTECTIONS</text>
  <circle class="badge-circle" cx="63" cy="740" r="45"/>
  <text class="badge-name" x="63" y="737" font-size="14">TALVON</text>
  <text class="badge-name" x="63" y="753" font-size="9">GUARD DOORS</text>
</svg>

<svg class="panel row-top col-4" viewBox="0 0 127 925" preserveAspectRatio="none">
  <rect width="127" height="925" fill="url(#grad-yellow)"/>
  <path class="fill-black" d="M0,0H127V70C90,72 40,55 0,55Z"/>
  <path class="fill-black" d="M0,65C40,80 80,105 127,95V125C80,128 40,110 0,85Z"/>
  <path class="fill-black" d="M0,875C30,815 80,790 127,788V860C80,862 30,870 0,880Z"/>
  <path class="fill-black" d="M0,890C45,880 90,880 127,885V925H0Z"/>
  <text class="panel-title fill-black" transform="translate(79,644) rotate(-90)" textLength="474" lengthAdjust="spacingAndGlyphs">MADE IN USA</text>
  <circle class="badge-circle" cx="61" cy="734" r="45"/>
  <text class="badge-name" x="61" y="731" font-size="14">TALVON</text>
  <text class="badge-name" x="61" y="747" font-size="9">GUARD DOORS</text>
</svg>

<svg class="panel row-top col-5" viewBox="0 0 127 925" preserveAspectRatio="none">
  <rect width="127" height="925" fill="url(#grad-black)"/>
  <path class="fill-yellow" d="M0,0H127V28C80,18 35,18 0,25Z"/>
  <path class="fill-yellow" d="M0,88C35,60 90,58 127,68V40C90,30 40,35 0,60Z"/>
  <path class="fill-yellow" d="M0,820C30,850 80,855 127,840V865C80,872 30,868 0,870Z"/>
  <path class="fill-yellow" d="M0,895C45,880 95,875 127,880V925H0Z"/>
  <text class="panel-title fill-yellow" transform="translate(81,696) rotate(-90)" textLength="592" lengthAdjust="spacingAndGlyphs">SECURITY GATES</text>
  <circle class="badge-circle" cx="63" cy="765" r="45"/>
  <text class="badge-name" x="63" y="762" font-size="14">TALVON</text>
  <text class="badge-name" x="63" y="778" font-size="9">GUARD DOORS</text>
</svg>

<svg class="panel row-top col-6" viewBox="0 0 127 925" preserveAspectRatio="none">
  <rect width="127" height="925" fill="url(#grad-yellow)"/>
  <path class="fill-black" d="M0,0H127V35C80,45 35,45 0,40Z"/>
  <path class="fill-black" d="M0,135C55,140 95,100 127,50V0H127V50C95,90 50,130 0,138Z"/>
  <path class="fill-black" d="M0,100C40,105 95,80 127,45V120C90,140 45,140 0,140Z"/>
  <path class="fill-black" d="M0,785C50,775 100,810 127,835V860C90,852 45,860 0,862Z"/>
  <path class="fill-black" d="M0,878C45,875 95,880 127,890V925H0Z"/>
  <text class="panel-title fill-black" transform="translate(80,642) rotate(-90)" textLength="482" lengthAdjust="spacingAndGlyphs">GARAGE DOORS</text>
  <circle class="badge-circle" cx="63" cy="719" r="45"/>
  <text class="badge-name" x="63" y="716" font-size="14">TALVON</text>
  <text class="badge-name" x="63" y="732" font-size="9">GUARD DOORS</text>
</svg>

<!-- Row 2 -->
<svg class="panel row-bottom col-1" viewBox="0 0 127 937" preserveAspectRatio="none">
  <rect width="127" height="937" fill="url(#grad-yellow)"/>
  <path class="fill-black" d="M0,0H127V28C80,40 35,60 0,62Z"/>
  <path class="fill-black" d="M0,95C45,95 95,80 127,65V92C85,110 40,140 0,145Z"/>
  <path class="fill-black" d="M0,850C40,825 95,825 127,835V855C90,850 40,855 0,870Z"/>
  <path class="fill-black" d="M0,880C40,870 95,880 127,888V937H0Z"/>
  <text class="panel-title fill-black" transform="translate(82,692) rotate(-90)" textLength="516" lengthAdjust="spacingAndGlyphs">ENTRY DOORS</text>
  <circle class="badge-circle" cx="64" cy="762" r="45"/>
  <text class="badge-name" x="64" y="759" font-size="14">TALVON</text>
  <text class="badge-name" x="64" y="775" font-size="9">GUARD DOORS</text>
</svg>

<svg class="panel row-bottom col-2" viewBox="0 0 127 937" preserveAspectRatio="none">
  <rect width="127" height="937" fill="url(#grad-black)"/>
  <path class="fill-yellow" d="M0,0H127V55C80,55 35,25 0,25Z"/>
  <path class="fill-yellow" d="M0,65C40,75 90,95 127,88V60C90,70 40,45 0,40Z"/>
  <path class="fill-yellow" d="M0,840C45,830 95,835 127,850V868C90,858 45,855 0,860Z"/>
  <path class="fill-yellow" d="M0,875C45,870 95,885 127,900V937H0Z"/>
  <text class="panel-title fill-yellow" transform="translate(83,689) rotate(-90)" textLength="545" lengthAdjust="spacingAndGlyphs">GATES GRILLS</text>
  <circle class="badge-circle" cx="63" cy="762" r="45"/>
  <text class="badge-name" x="63" y="759" font-size="14">TALVON</text>
  <text class="badge-name" x="63" y="775" font-size="9">GUARD DOORS</text>
</svg>

<svg class="panel row-bottom col-3" viewBox="0 0 127 937" preserveAspectRatio="none">
  <rect width="127" height="937" fill="url(#grad-yellow)"/>
  <path class="fill-black" d="M0,25C40,15 90,15 127,22V35C90,32 40,35 0,45Z"/>
  <path class="fill-black" d="M0,60C40,40 90,45 127,60V105C90,80 40,70 0,80Z"/>
  <path class="fill-black" d="M0,830C45,805 95,800 127,810V840C90,835 40,840 0,850Z"/>
  <path class="fill-black" d="M0,860C45,855 95,880 127,878V900C90,905 40,900 0,905Z"/>
  <text class="panel-title fill-black" transform="translate(83,670) rotate(-90)" textLength="533" lengthAdjust="spacingAndGlyphs">PATIO DOORS</text>
  <circle class="badge-circle" cx="63" cy="742" r="45"/>
  <text class="badge-name" x="63" y="739" font-size="14">TALVON</text>
  <text class="badge-name" x="63" y="755" font-size="9">GUARD DOORS</text>
</svg>

<svg class="panel row-bottom col-4" viewBox="0 0 127 937" preserveAspectRatio="none">
  <rect width="127" height="937" fill="url(#grad-black)"/>
  <path class="fill-yellow" d="M0,0H127V50C80,60 40,50 0,50Z"/>
  <path class="fill-yellow" d="M0,95C35,95 90,110 127,85V105C90,130 40,125 0,120Z"/>
  <path class="fill-yellow" d="M0,830C45,810 95,815 127,830V845C90,835 45,835 0,850Z"/>
  <path class="fill-yellow" d="M0,855C40,845 90,860 127,870V937H0Z"/>
  <text class="panel-title fill-yellow" transform="translate(81,672) rotate(-90)" textLength="542" lengthAdjust="spacingAndGlyphs">ROLLING STEEL</text>
  <circle class="badge-circle" cx="63" cy="747" r="45"/>
  <text class="badge-name" x="63" y="744" font-size="14">TALVON</text>
  <text class="badge-name" x="63" y="760" font-size="9">GUARD DOORS</text>
</svg>

<svg class="panel row-bottom col-5" viewBox="0 0 127 937" preserveAspectRatio="none">
  <rect width="127" height="937" fill="url(#grad-yellow)"/>
  <path class="fill-black" d="M0,0H127V60C90,55 40,45 0,50Z"/>
  <path class="fill-black" d="M0,80C35,65 90,85 127,95V125C90,105 40,85 0,95Z"/>
  <path class="fill-black" d="M0,815C30,850 80,860 127,855V890C80,895 30,890 0,895Z"/>
  <path class="fill-black" d="M0,910C45,900 95,905 127,912V937H0Z"/>
  <text class="panel-title fill-black" transform="translate(84,707) rotate(-90)" textLength="560" lengthAdjust="spacingAndGlyphs">WINDOW BARS</text>
  <circle class="badge-circle" cx="63" cy="781" r="45"/>
  <text class="badge-name" x="63" y="778" font-size="14">TALVON</text>
  <text class="badge-name" x="63" y="794" font-size="9">GUARD DOORS</text>
</svg>

<svg class="panel row-bottom col-6" viewBox="0 0 127 937" preserveAspectRatio="none">
  <rect width="127" height="937" fill="url(#grad-black)"/>
  <path class="fill-yellow" d="M0,0H127V25C80,20 35,25 0,35Z"/>
  <path class="fill-yellow" d="M0,118C45,90 80,50 127,45V25C80,30 40,80 0,108Z"/>
  <path class="fill-yellow" d="M0,820C45,815 95,840 127,870V890C90,865 45,850 0,855Z"/>
  <path class="fill-yellow" d="M0,880C40,885 90,910 127,915V937H0Z"/>
  <text class="panel-title fill-yellow" transform="translate(82,672) rotate(-90)" textLength="544" lengthAdjust="spacingAndGlyphs">STORM DOORS</text>
  <circle class="badge-circle" cx="63" cy="748" r="45"/>
  <text class="badge-name" x="63" y="745" font-size="14">TALVON</text>
  <text class="badge-name" x="63" y="761" font-size="9">GUARD DOORS</text>
</svg>

</body>
</html>
```